Optometric Practice needs Initial Photoshop Mockup

We need a graphic design for the homepage of a website for an optometric practice that specializes in vision therapy.

Here's the link to the project folder on Stashvale. I've included photos, example sites, content and instructions.

https://www.stashvale.example/sh/kx7rm2wq8zn41d9/BBQ_LmTyRwoPvXe3NcDrKuWjz

Please feel free to submit any questions about the design. I'll be happy to help guide you in any areas you're uncertain of.

Okay - I've updated the project to payment confirmed. Let's see some designs :) Thanks, Reg

```html
<!DOCTYPE html>
<html lang="en">
<head>
<meta charset="utf-8">
<title>Clearview Learning Centers — Home</title>
<link href="https://fonts.googleapis.com/css2?family=Mulish:wght@400;600;700;800&family=Open+Sans:ital,wght@0,400;0,600;0,700;1,400&display=swap" rel="stylesheet">
<style>
:root{
  --navy:#101c3a;
  --red:#8c0c0c;
  --link:#2b2bd9;
  --nav-line:#4747b8;
  --hero-bg:#e9e9e9;
  --text:#333;
  --muted:#666;
  --rule:#d4d4d4;
  --footer-bg:#ebebeb;
}
*{margin:0;padding:0;box-sizing:border-box}
html,body{width:895px;height:1200px;overflow:hidden;background:#fff}
body{position:relative;font-family:"Mulish",sans-serif;color:var(--text)}
.abs{position:absolute}
.topbar{left:0;top:0;width:895px;height:27px;background:var(--navy)}
.topbar .phone{right:82px;top:5px;color:#fff;font-size:12.5px;display:flex;align-items:center;gap:7px}
.hero{left:0;top:27px;width:895px;height:415px;background:var(--hero-bg);border-bottom:1px solid #ccc}
.brand{left:84px;top:19px;font-size:26px;font-weight:800;color:var(--red);letter-spacing:.5px}
.nav{left:298px;top:24px;width:515px;height:23px;border-bottom:1.5px solid var(--nav-line);display:flex;justify-content:space-between;font-size:9.6px;color:#888;letter-spacing:-.2px}
.nav a{color:inherit;text-decoration:none;padding:0 4px;height:23px}
.nav a.active{color:var(--red);border-bottom:2px solid #b86}
.hero h1{left:82px;top:136px;width:340px;font-size:19px;font-weight:400;color:var(--red);white-space:nowrap;letter-spacing:-.2px}
.hero h1 b{font-weight:800}
.hero .lede{left:82px;top:179px;width:335px;font-size:9.6px;line-height:17.6px;color:#444}
.btn{top:279px;height:31px;border-radius:3px;font-size:10px;font-weight:700;display:flex;align-items:center;justify-content:center;white-space:nowrap}
.btn.primary{left:82px;width:150px;background:var(--red);color:#fff}
.btn.outline{left:248px;width:133px;border:1px solid #222;color:#111}
.video{left:438px;top:105px;width:375px;height:256px;background:linear-gradient(135deg,#4a5160,#7a5a7c 45%,#3a3f4c)}
.dots{left:412px;top:390px;display:flex;gap:12px}
.dots i{width:10px;height:10px;border-radius:50%;background:#fff}
.dots i.on{background:var(--red)}
.welcome h2{left:82px;top:471px;font-size:17.6px;font-weight:400;color:#333}
.welcome p{left:82px;top:501px;width:732px;font-size:9.6px;line-height:18px;color:#777}
.photo{border-radius:50%;background:radial-gradient(circle at 50% 40%,#d9c4b4,#8a7a70)}
.ask{left:162px;top:570px;font-size:16px;color:var(--red);line-height:26px;white-space:nowrap}
.ask b{font-weight:800}
.more{font-size:10px;color:var(--link)}
.stories{left:83px;top:671px;font-size:17.6px;font-weight:400;color:#111}
.quotemark{left:212px;top:658px;font-size:48px;color:#aaa;font-family:Georgia,serif;font-weight:700}
.quote{left:82px;top:714px;width:202px;height:182px;background:#ececec;padding:24px 18px 0 24px;font-family:"Open Sans",sans-serif;font-style:italic;font-size:11px;line-height:16.4px;color:#555}
.patient{left:189px;top:901px;font-size:10px;line-height:14px;color:#111}
.vrule{width:1px;background:var(--rule);top:560px;height:412px}
.hrule{height:1px;background:var(--rule);top:765px}
.card{width:160px;text-align:center}
.card .pic{width:96px;height:96px;margin:0 auto}
.card h3{margin:13px auto 0;width:110px;font-size:10px;font-weight:600;color:#111;padding-bottom:4px;border-bottom:1px solid var(--rule);white-space:nowrap;display:flex;justify-content:center}
.card p{margin-top:5px;font-size:9.2px;line-height:16.5px;color:#555}
.card .more{display:block;margin-top:7px}
.footer{left:0;top:1010px;width:895px;height:190px;background:var(--footer-bg);font-family:"Open Sans",sans-serif}
.footer h4{font-size:13px;font-weight:700;color:#555;letter-spacing:.3px}
.contact{left:114px;top:30px}
.rows{margin-top:6px;font-size:9px;color:#444;line-height:17px}
.rows .r{display:flex}
.rows .k{width:42px}
.rows .c{width:11px}
.rows .v{line-height:14px;padding-top:1.5px}
.fdiv{top:24px;width:1px;height:148px;background:#bbb}
.touch{left:378px;top:30px}
.socials{display:flex;gap:5px;margin-top:8px}
.socials i{width:26px;height:26px;border-radius:50%;background:#555;display:flex;align-items:center;justify-content:center}
.subscribe{margin-top:12px;font-size:10.4px;color:#444}
.signup{margin-top:7px;display:flex;height:24px}
.signup span{width:132px;background:#fff;font-size:9px;padding:7px 9px;color:#222}
.signup b{width:26px;background:#f6f6f6;font-weight:400;font-size:10px;color:#555;display:flex;align-items:center;justify-content:center}
.flogo{left:606px;top:48px;font-size:26px;font-weight:800;color:#555;font-family:"Mulish",sans-serif}
.copy{left:617px;top:120px;font-size:9px;color:#333}
</style>
</head>
<body>

<div class="abs topbar">
  <div class="abs phone">
    <svg width="17" height="17" viewBox="0 0 20 20"><circle cx="10" cy="10" r="9" fill="none" stroke="#fff" stroke-width="1.4"/><path d="M7 5.5l1.6 2.2-1 1.2c.7 1.4 1.6 2.3 3 3l1.2-1 2.2 1.6-.9 1.6c-3.6-.3-6.6-3.3-6.9-6.9z" fill="#fff"/></svg>
    410-555-0142
  </div>
</div>

<section class="abs hero">
  <div class="abs brand">Clearview</div>
  <nav class="abs nav">
    <a class="active">Home</a><a>Meet Us</a><a>New Patients</a><a>Vision &amp; Learning</a><a>Vision Therapy</a><a>Head Injuries</a><a>Professionals</a><a>Contact Us</a>
  </nav>
  <h1 class="abs">Improving <b>VISION,</b> Changing <b>LIVES</b></h1>
  <p class="abs lede">Lorem ipsum dolor sit amet, consectetuer adipiscing elit, sed diam non-ummy nibh euismod tincidunt ut laoreet dolore magna aliquam erat volut-pat. Ut wisi enim ad minim veniam, quis nostrud exerci tation ullamcorper suscipit lobortis nisl ut aliquip ex ea commodo consequat.</p>
  <div class="abs btn primary">Learn More About Clearview</div>
  <div class="abs btn outline">Request An Appointment</div>
  <div class="abs video" role="img" aria-label="Television news interview video with two presenters at a studio desk">
    <svg class="abs" style="left:174px;top:105px" width="26" height="30" viewBox="0 0 26 30"><path d="M2 2l22 13L2 28z" fill="#fff"/></svg>
  </div>
  <div class="abs dots"><i></i><i class="on"></i><i></i><i></i></div>
</section>

<section class="welcome">
  <h2 class="abs">Welcome To Clearview Learning Centers, Inc.</h2>
  <p class="abs">Lorem ipsum dolor sit amet, consectetuer adipiscing elit, sed diam nonummy nibh euismod tincidunt ut laoreet dolore magna aliquam erat volutpat. Ut wisi enim ad minim veniam, quis nostrud exerci tation ullamcorper suscipit lobortis nisl ut aliquip ex ea commodo consequat.</p>
</section>

<div class="abs photo" style="left:83px;top:572px;width:68px;height:68px" role="img" aria-label="Photo of a tired young child"></div>
<div class="abs ask">Does my child have a<br><b>VISION PROBLEM?</b></div>
<div class="abs more" style="left:160px;top:627px">Read More...</div>

<div class="abs stories">Success Stories</div>
<div class="abs quotemark">“</div>
<div class="abs quote">Cras malesuada nisi sed tellus fringilla commodo. Cras dictum purus sit amet dolor auctor, at facilisis tortor euismod. Mauris aliquet a nunc tempus dictum. Nullam interdum neque sit amet condimentum congue.</div>
<div class="abs photo" style="left:111px;top:870px;width:69px;height:69px;border:2px solid #fff" role="img" aria-label="Portrait of a smiling patient"></div>
<div class="abs patient">MAREN HOLT<br><b style="font-weight:600">Patient</b></div>
<div class="abs more" style="left:83px;top:957px">Success with Vision Therapy...</div>

<div class="abs vrule" style="left:322px"></div>
<div class="abs vrule" style="left:488px"></div>
<div class="abs vrule" style="left:658px"></div>
<div class="abs hrule" style="left:334px;width:134px"></div>
<div class="abs hrule" style="left:506px;width:136px"></div>
<div class="abs hrule" style="left:672px;width:136px"></div>

<div class="abs card" style="left:322px;top:558px">
  <div class="pic photo" role="img" aria-label="Optometrist examining a patient with eye equipment"></div>
  <h3>EYE EXAMINATION</h3>
  <p>lorem ipsum dolor sit amet<br>consectutuer adpicsing diam set</p>
  <span class="more">Read More...</span>
</div>
<div class="abs card" style="left:491px;top:558px">
  <div class="pic photo" role="img" aria-label="Child focusing on a vision therapy tool"></div>
  <h3>VISION THERAPY</h3>
  <p>lorem ipsum dolor sit amet<br>consectutuer adpicsing diam set</p>
  <span class="more">Read More...</span>
</div>
<div class="abs card" style="left:659px;top:558px">
  <div class="pic photo" role="img" aria-label="Frustrated student holding her head"></div>
  <h3>LEARNING PROBLEMS</h3>
  <p>lorem ipsum dolor sit amet<br>consectutuer adpicsing diam set</p>
  <span class="more">Read More...</span>
</div>
<div class="abs card" style="left:322px;top:787px">
  <div class="pic photo" role="img" aria-label="Woman reading a document"></div>
  <h3>HIDDEN DISABILITY</h3>
  <p>lorem ipsum dolor sit amet<br>consectutuer adpicsing diam set</p>
  <span class="more">Read More...</span>
</div>
<div class="abs card" style="left:491px;top:787px">
  <div class="pic photo" role="img" aria-label="Child covering one eye"></div>
  <h3>AMBLYOPIA OR LAZY EYE</h3>
  <p>lorem ipsum dolor sit amet<br>consectutuer adpicsing diam set</p>
  <span class="more">Read More...</span>
</div>
<div class="abs card" style="left:659px;top:787px">
  <div class="pic photo" style="background:radial-gradient(circle at 50% 40%,#9aa38a,#5e6e48)" role="img" aria-label="Baseball batter at home plate"></div>
  <h3>SPORTS VISION</h3>
  <p>lorem ipsum dolor sit amet<br>consectutuer adpicsing diam set</p>
  <span class="more">Read More...</span>
</div>

<footer class="abs footer">
  <div class="abs contact">
    <h4>CONTACT US</h4>
    <div class="rows">
      <div class="r"><span class="k">Phone</span><span class="c">:</span><span>410-555-0142</span></div>
      <div class="r"><span class="k">Email</span><span class="c">:</span><span>hello@clearview.example</span></div>
      <div class="r"><span class="k">Address</span><span class="c">:</span><span class="v">4410 Harbor Ridge Pkwy.<br>Lakeside Commons, Ste. 3<br>Marlow, MD, 21099</span></div>
    </div>
  </div>
  <div class="abs fdiv" style="left:347px"></div>
  <div class="abs touch">
    <h4>GET IN TOUCH</h4>
    <div class="socials">
      <i></i><i></i><i></i>
      <i><svg width="14" height="10" viewBox="0 0 14 10"><rect x=".6" y=".6" width="12.8" height="8.8" fill="none" stroke="#fff" stroke-width="1.2"/><path d="M.6.6L7 6l6.4-5.4" fill="none" stroke="#fff" stroke-width="1.2"/></svg></i>
    </div>
    <div class="subscribe">Subscribe monthly Newsletter</div>
    <div class="signup"><span>Enter your email address</span><b>GO</b></div>
  </div>
  <div class="abs fdiv" style="left:572px"></div>
  <div class="abs flogo">Clearview</div>
  <div class="abs copy">Copyright © 2014 . All rights Reserved</div>
</footer>

</body>
</html>
```